Lena Business card

This card is to represent me as a coach and Vivamora facilitator
Double sided in colour
A beautiful, simple and elegant design that indicates movement and is modern, FRESH and uplifting. Please don’t use much black and use the attached Vivamora logo.
Preferred colours - white, lighter blues and fresh greens

Target Market(s)
Business people - potential clients age 35 up
Industry/Entity Type
Business
Requirements
Must have
-  Text for the front :
Lumivera Living
Lena Darrow
Biocentric Coach
Co-Director, Vivamora School of Australia
E: lena@vivamora.com.au
M: 0471 552 908.
W: vivamora.com.au
Biocentric Coaching for Individuals, Teams and Organisations
Vivamora for Children, Adults and Social development projects
Text for the back :
The Vivamora system facilitates the expression of human potential for health, happiness and humanity through music, movement and group interaction. It was developed by Emilio Vasca Orduña, a Chilean anthropologist and clinical psychologist, in 1976.
Creative use of the logo - integrating it within the design - e.g perhaps using it as the O in Vivamora,
Please feature the heron from the logo or a another elegant graceful stylized heron.

```html
<!DOCTYPE html>
<html lang="en">
<head>
<meta charset="utf-8">
<title>Lena Darrow – Business Card</title>
<link rel="stylesheet" href="https://fonts.googleapis.com/css2?family=Open+Sans:wght@400;600&display=swap">
<style>
  :root {
    --stage: #ecebe7;
    --green-deep: #67a82a;
    --green-light: #a9d45c;
    --green-text: #7cb133;
    --orange: #e8731f;
    --ink: #5b5b5b;
    --paper: #ffffff;
  }
  * { margin: 0; padding: 0; box-sizing: border-box; }
  html, body {
    width: 1200px; height: 676px; overflow: hidden;
    background: var(--stage);
    font-family: "Open Sans", Arial, sans-serif;
  }
  .sheet {
    position: relative; width: 1200px; height: 676px;
    display: flex; align-items: center; justify-content: center; gap: 40px;
  }
  .card {
    position: relative; width: 540px; height: 310px;
    box-shadow: 0 6px 18px rgba(0,0,0,0.18);
    overflow: hidden;
  }
  /* Back side */
  .card-back {
    background: linear-gradient(135deg, var(--green-deep) 0%, var(--green-light) 75%);
  }
  .card-back__mark {
    position: absolute; left: 150px; top: 120px;
    font-size: 64px; font-weight: 400; color: #ffffff; opacity: 0.12;
    letter-spacing: 2px;
  }
  .card-back__about {
    position: absolute; left: 150px; top: 52px; width: 340px;
    color: #ffffff; font-size: 13.5px; line-height: 1.42;
    text-align: justify;
  }
  /* Front side */
  .card-front { background: var(--paper); }
  .identity { position: absolute; left: 40px; top: 96px; }
  .identity__name { color: var(--orange); font-size: 20px; font-weight: 400; }
  .identity__role { color: var(--green-text); font-size: 12.5px; line-height: 1.4; margin-top: 2px; }
  .contacts { position: absolute; left: 40px; top: 168px; list-style: none; }
  .contacts li {
    display: flex; align-items: center; gap: 8px;
    color: var(--ink); font-size: 12.5px; line-height: 1.75;
  }
  .contacts svg { width: 10px; height: 10px; flex: none; }
  .brand {
    position: absolute; right: 38px; top: 70px;
    width: 170px; height: 170px;
    display: flex; align-items: center; justify-content: center;
  }
  .brand__ring { position: absolute; inset: 0; }
  .brand__name { color: var(--orange); font-size: 22px; font-weight: 400; letter-spacing: 1px; }
</style>
</head>
<body>
<main class="sheet">
  <section class="card card-back" aria-label="Card back">
    <span class="card-back__mark" aria-hidden="true">Vivamora</span>
    <p class="card-back__about">The Vivamora system facilitates the expression of human potential for health, happiness and humanity through music, movement and group interaction. It was developed by Emilio Vasca Orduña, a Chilean anthropologist and clinical psychologist in 1976.</p>
  </section>

  <section class="card card-front" aria-label="Card front">
    <div class="identity">
      <h1 class="identity__name">Lena Darrow</h1>
      <p class="identity__role">Biocentric Coach<br>Co-director Vivamora School of Australia</p>
    </div>
    <ul class="contacts">
      <li>
        <svg viewBox="0 0 10 10" aria-hidden="true"><rect x="2.5" y="0.5" width="5" height="9" rx="1" fill="none" stroke="#e8731f" stroke-width="1.2"/></svg>
        0471 552 908
      </li>
      <li>
        <svg viewBox="0 0 10 10" aria-hidden="true"><rect x="0.6" y="2" width="8.8" height="6" fill="none" stroke="#e8731f" stroke-width="1.1"/><path d="M0.6 2 L5 5.5 L9.4 2" fill="none" stroke="#e8731f" stroke-width="1.1"/></svg>
        lena@vivamora.com.au
      </li>
      <li>
        <svg viewBox="0 0 10 10" aria-hidden="true"><circle cx="5" cy="5" r="4.3" fill="none" stroke="#e8731f" stroke-width="1.1"/><path d="M0.7 5 H9.3 M5 0.7 C2.5 3 2.5 7 5 9.3 M5 0.7 C7.5 3 7.5 7 5 9.3" fill="none" stroke="#e8731f" stroke-width="0.9"/></svg>
        vivamora.com.au
      </li>
    </ul>
    <div class="brand">
      <svg class="brand__ring" viewBox="0 0 170 170" aria-hidden="true"><circle cx="85" cy="85" r="82" fill="none" stroke="#e8731f" stroke-width="1.2"/></svg>
      <span class="brand__name">Vivamora</span>
    </div>
  </section>
</main>
</body>
</html>
```